Email Signiture and letterhead design

we are looking for a modern business design to incorporate our logo and qel certification plus social icons for Vorlant, Pelmora, and zandoro
they must include our UK vat and also company registration as text but I can fill these out. Email signature to have a link/icon to our webshop www.trexolan.co.uk

Target Market(s)

All

Font styles to use
Serif
Sans Serif

Requirements
Must have
• Address, tel, email , web details incorperated
Nice to have
• a professional looking letter head and email signiture, Email signature to have a link/icon to our webshop www.trexolan.co.uk

```html
<!DOCTYPE html>
<html lang="en">
<head>
<meta charset="utf-8">
<title>Trexolan Axles Ltd – Letterhead</title>
<link href="https://fonts.googleapis.com/css2?family=Open+Sans:wght@400;600&display=swap" rel="stylesheet">
<style>
  :root {
    --backdrop: #dedede;
    --paper: #f8f8f8;
    --ink: #555555;
    --ink-dark: #3a3a3a;
    --brand-red: #e3202a;
    --signature-blue: #1b2a4a;
    --badge-pink: #e0177f;
    --badge-grey: #ececec;
  }
  * { box-sizing: border-box; margin: 0; padding: 0; }
  html, body {
    width: 1153px; height: 1200px; overflow: hidden;
    background: var(--backdrop);
    font-family: "Open Sans", Arial, sans-serif;
  }
  .letterhead {
    position: absolute; left: 160px; top: 20px;
    width: 834px; height: 1160px;
    background: var(--paper);
    box-shadow: 0 14px 40px rgba(0,0,0,0.14);
    color: var(--ink);
  }
  .brand {
    position: absolute; left: 83px; top: 92px;
    display: flex; align-items: center; gap: 10px;
  }
  .brand-dot { width: 20px; height: 20px; border-radius: 50%; background: var(--brand-red); }
  .brand-name { font-size: 22px; font-weight: 600; color: var(--ink-dark); letter-spacing: 0.5px; }
  .contact {
    position: absolute; left: 573px; top: 68px;
    font-size: 13.5px; line-height: 17.5px; color: var(--ink-dark);
    font-style: normal;
  }
  .contact-address { margin-bottom: 6px; }
  .contact-line { display: flex; align-items: center; gap: 7px; }
  .contact-line svg { width: 13px; height: 13px; fill: var(--brand-red); flex: none; }
  .letter-body {
    position: absolute; left: 83px; top: 290px; width: 668px;
    font-size: 14.6px; line-height: 22px;
  }
  .letter-body p { margin-bottom: 22px; text-align: justify; }
  .letter-body .salutation { margin-bottom: 22px; text-align: left; }
  .signature {
    width: 96px; height: 90px; margin-top: -6px;
    background: linear-gradient(135deg, rgba(27,42,74,0.18), rgba(27,42,74,0.05));
    border-radius: 4px;
  }
  .registry {
    position: absolute; left: 83px; top: 1074px;
    font-size: 14px; line-height: 20px; color: var(--ink-dark);
  }
  .certification-badge {
    position: absolute; left: 595px; top: 1037px;
    width: 153px; height: 55px;
    border: 1.5px solid #444; border-radius: 10px;
    background: linear-gradient(to right, var(--badge-grey) 85%, var(--badge-pink) 85%);
  }
</style>
</head>
<body>
  <main class="letterhead">
    <header>
      <div class="brand">
        <span class="brand-dot"></span>
        <span class="brand-name">Trexolan Axles Ltd</span>
      </div>
      <address class="contact">
        <div class="contact-address">Morvel Strasse 4 09318<br>City Haldenau Germany</div>
        <div class="contact-line">
          <svg viewBox="0 0 16 16" aria-hidden="true"><path d="M3 2h3l1.5 3.5-2 1.2a8 8 0 0 0 3.8 3.8l1.2-2L14 10v3a1 1 0 0 1-1 1A11 11 0 0 1 2 3a1 1 0 0 1 1-1z"/></svg>
          555.014.2290
        </div>
        <div class="contact-line">
          <svg viewBox="0 0 16 16" aria-hidden="true"><path d="M1 3h14v2L8 9 1 5z"/><path d="M1 6.5l7 4 7-4V13H1z"/></svg>
          info@trexolan.co.uk
        </div>
        <div class="contact-line">
          <svg viewBox="0 0 16 16" aria-hidden="true"><circle cx="8" cy="8" r="7"/></svg>
          www.trexolan.co.uk
        </div>
      </address>
    </header>

    <section class="letter-body">
      <p class="salutation">Dear customer,</p>
      <p>Lorem ipsum dolor sit amet, consectetur adipisicing elit, sed do eiusmod tempor incididunt ut labore et dolore magna aliqua. Ut enim ad minim veniam, quis nostrud exercitation ullamco laboris nisi ut aliquip ex ea commodo consequat. Duis aute irure dolor in reprehenderit in voluptate velit esse cillum dolore eu fugiat nulla pariatur. Excepteur sint occaecat cupidatat non proident, sunt in culpa qui officia deserunt mollit anim id est laborum.</p>
      <p>Lorem ipsum dolor sit amet, consectetur adipisicing elit, sed do eiusmod tempor incididunt ut labore et dolore magna aliqua. Ut enim ad minim veniam, quis nostrud exercitation ullamco laboris nisi ut aliquip ex ea commodo consequat. Duis aute irure dolor in reprehenderit in voluptate velit esse cillum dolore eu fugiat nulla pariatur. Excepteur sint occaecat cupidatat non proident, sunt in culpa qui officia deserunt mollit anim id est laborum.</p>
      <p>Lorem ipsum dolor sit amet, consectetur adipisicing elit, sed do eiusmod tempor incididunt ut labore et dolore magna aliqua. Ut enim ad minim veniam, quis nostrud exercitation ullamco laboris nisi ut aliquip ex ea commodo consequat. Duis aute irure dolor in reprehenderit in voluptate velit esse cillum dolore eu fugiat nulla pariatur. Excepteur sint occaecat cupidatat non proident, sunt in culpa qui officia deserunt mollit anim id est laborum.</p>
      <p>Lorem ipsum dolor sit amet, consectetur adipisicing elit, sed do eiusmod tempor incididunt ut labore et dolore magna aliqua. Ut enim ad minim veniam, quis nostrud exercitation ullamco laboris nisi ut aliquip ex ea commodo consequat. Duis aute irure dolor in reprehenderit.</p>
      <p class="salutation">Yours Sincerely,</p>
      <div class="signature" role="img" aria-label="Handwritten signature"></div>
    </section>

    <footer>
      <div class="registry">
        VAT : 3302 6617 8840<br>
        Registration : 0861 2754 3309
      </div>
      <div class="certification-badge" role="img" aria-label="Quality management certification badge"></div>
    </footer>
  </main>
</body>
</html>
```